Health Information/Education Logo Design

We need a logo design for a new company based in Atlanta called Meadowlark Health. The program is about patient empowerment. We provide health information and education on how to get healthy, stay healthy, and how to be proactive in your care. We also provide medication and injection training to help patients feel their best and to ensure successful therapy outcomes.
We like the colors yellow, pink, teal and purple and would like to see some or all of these colors in the designs. The final design should communicate caring, considerate, compassionate information, education and training services
Industry/Entity Type
Education
Contact Information for Business Card
Meadowlark Health
Danielle Ostrander RN, MSN, MHA
Nurse Educator
555.214.3096 cell
555.470.2283 fax

```html
<!DOCTYPE html>
<html lang="en">
<head>
<meta charset="utf-8">
<title>Meadowlark Health Business Card</title>
<link rel="stylesheet" href="https://fonts.googleapis.com/css2?family=Cinzel:wght@600&family=Lato:wght@400&display=swap">
<style>
  :root {
    --backdrop: #e9e6e2;
    --card: #ffffff;
    --purple: #5b3f98;
    --pink: #e0509f;
    --ink: #333340;
    --divider: #b9b2cc;
  }
  * { margin: 0; padding: 0; box-sizing: border-box; }
  html, body { width: 1200px; height: 891px; overflow: hidden; }
  body { background: var(--backdrop); position: relative; font-family: "Lato", Arial, sans-serif; }

  .card {
    position: absolute;
    width: 560px;
    height: 320px;
    background: var(--card);
    border-radius: 18px;
    box-shadow: 0 8px 24px rgba(0,0,0,0.18);
    overflow: hidden;
  }
  .card--front { left: 70px; top: 90px; }
  .card--back { left: 570px; top: 480px; }

  .brand {
    position: absolute;
    display: flex;
    align-items: center;
    gap: 14px;
  }
  .brand__dot {
    width: 22px; height: 22px;
    border-radius: 50%;
    background: var(--pink);
    flex: none;
  }
  .brand__name {
    font-family: "Cinzel", Georgia, serif;
    font-weight: 600;
    font-size: 30px;
    color: var(--purple);
    white-space: nowrap;
  }
  .card--front .brand { left: 50%; top: 50%; transform: translate(-50%, -50%); }
  .card--back .brand { left: 50%; top: 96px; transform: translateX(-50%); }

  .tab {
    position: absolute;
    width: 14px;
    height: 62px;
    background: var(--purple);
  }
  .tab--top-right { right: 0; top: 26px; border-radius: 4px 0 0 4px; }
  .tab--bottom-left { left: 0; bottom: 26px; border-radius: 0 4px 4px 0; }

  .person {
    position: absolute;
    left: 48px;
    bottom: 48px;
  }
  .person__name { font-size: 19px; color: var(--purple); }
  .person__title { font-size: 14px; color: var(--pink); margin-top: 3px; text-align: right; }

  .divider {
    position: absolute;
    left: 326px;
    bottom: 44px;
    width: 1px;
    height: 56px;
    background: var(--divider);
  }

  .contact {
    position: absolute;
    left: 346px;
    bottom: 50px;
    font-size: 13px;
    color: var(--ink);
    line-height: 1.8;
  }
  .contact__label { color: var(--purple); display: inline-block; width: 18px; }
</style>
</head>
<body>
  <section class="card card--front" aria-label="Card front">
    <div class="brand">
      <span class="brand__dot"></span>
      <span class="brand__name">Meadowlark Health</span>
    </div>
  </section>

  <section class="card card--back" aria-label="Card back">
    <span class="tab tab--top-right"></span>
    <span class="tab tab--bottom-left"></span>
    <div class="brand">
      <span class="brand__dot"></span>
      <span class="brand__name">Meadowlark Health</span>
    </div>
    <div class="person">
      <p class="person__name">Danielle Ostrander RN, MSN</p>
      <p class="person__title">MHA Nurse Educator</p>
    </div>
    <span class="divider"></span>
    <div class="contact">
      <p><span class="contact__label">M</span>: 555.214.3096</p>
      <p><span class="contact__label">F</span>: 555.470.2283</p>
    </div>
  </section>
</body>
</html>
```